Lantern Hill Publicity is a new boutique Press Office with a small roster of well-chosen clients across an array of disciplines; from Art and Technology to Restaurants and Fashion. Based in Greenpoint Brooklyn, Lantern Hill Publicity achieves outstanding results through hard work, tenacity, efficiency and a sense of humor. We need a simple, versatile and classic design. We would like each side of the card to be white text on a black background.

Boutique

```html
<!DOCTYPE html>
<html lang="en">
<head>
<meta charset="utf-8">
<title>Lantern Hill Publicity — Business Card</title>
<link rel="stylesheet" href="https://fonts.googleapis.com/css2?family=Cormorant+Garamond:wght@500&family=Source+Sans+3:wght@400;600&display=swap">
<style>
  :root {
    --backdrop: #4f4f4f;
    --card-front: #161719;
    --card-back: #000000;
    --ink: #ffffff;
    --ink-soft: #e9e9e9;
  }
  * { margin: 0; padding: 0; box-sizing: border-box; }
  html, body { width: 1200px; height: 900px; overflow: hidden; }
  body {
    background: var(--backdrop);
    position: relative;
    font-family: "Source Sans 3", Arial, sans-serif;
    color: var(--ink);
  }
  .card {
    position: absolute;
    top: 170px;
    width: 347px;
    height: 560px;
    text-align: center;
  }
  .card--front { left: 259px; background: var(--card-front); }
  .card--back { left: 631px; background: var(--card-back); }

  .wordmark {
    position: absolute;
    left: 0; right: 0;
    font-family: "Cormorant Garamond", Georgia, serif;
    font-weight: 500;
    color: var(--ink);
    text-transform: uppercase;
  }
  .wordmark__name { display: block; font-size: 27px; letter-spacing: 0.16em; line-height: 1; }
  .wordmark__sub { display: block; font-size: 12px; letter-spacing: 0.42em; margin-top: 8px; padding-left: 0.42em; }
  .card--front .wordmark { top: 160px; }
  .card--back .wordmark { top: 292px; }
  .card--back .wordmark__name { font-size: 30px; }
  .card--back .wordmark__sub { font-size: 13px; }

  .contact { position: absolute; left: 0; right: 0; top: 308px; color: var(--ink-soft); }
  .contact__name { font-size: 21px; font-weight: 600; color: var(--ink); line-height: 1.2; }
  .contact__role { font-size: 14.5px; margin-top: 2px; }
  .contact__lines { list-style: none; margin-top: 22px; font-size: 14.5px; line-height: 21px; }
  .contact__lines b { font-weight: 600; color: var(--ink); }
  .contact__address { font-style: normal; margin-top: 17px; font-size: 14.5px; line-height: 17px; }
</style>
</head>
<body>
  <section class="card card--front" aria-label="Card front">
    <div class="wordmark">
      <span class="wordmark__name">Lantern Hill</span>
      <span class="wordmark__sub">Publicity</span>
    </div>
    <div class="contact">
      <p class="contact__name">MARA ELLISON</p>
      <p class="contact__role">Managing Director</p>
      <ul class="contact__lines">
        <li><b>P:</b> 555-014-2290</li>
        <li><b>E:</b> hello@lanternhillpr.com</li>
        <li><b>W:</b> www.lanternhillpr.com</li>
      </ul>
      <address class="contact__address">88 Kent Street, Greenpoint<br>Brooklyn, NY 11222</address>
    </div>
  </section>

  <section class="card card--back" aria-label="Card back">
    <div class="wordmark">
      <span class="wordmark__name">Lantern Hill</span>
      <span class="wordmark__sub">Publicity</span>
    </div>
  </section>
</body>
</html>
```